Modern Venture Capital website

Design a modern website for a venture capital firm. This website should be modern and beautiful and be on par with other Venture Capital websites. I have a logo and a hero video I'd like to use. Link to hero video: https://files.vantoria.example/f/9Xk2Lm7qPz4Rt8Wb3Nc6Hd5Jy1Gs0Ve/view?ref=share_link

Preference will be given to the best design that combines design with the best images and digital content. That means no generic free stock videos 😅

I currently built a wix website to give you an idea of what content needs to be on the website. Depending on your design it can be 3 pages, or one long page. I will leave it up to you.

WEBSITE: https://brelmor58204.pagecraftly.example/my-site-4

Target Market(s)

Mid-career professionals, individuals interested in Venture Capital

Industry/Entity Type

Finance, venture capital, startups

Requirements
Must have
• must use the hero video I have and must use my logo. Must use high quality images that matches the website design - no generic stock images

```html
<!DOCTYPE html>
<html lang="en">
<head>
<meta charset="utf-8">
<title>Lateshift Ventures</title>
<link href="https://fonts.googleapis.com/css2?family=Poppins:ital,wght@0,300;0,400;0,500;0,600;0,700;1,600;1,700&family=Figtree:wght@500;600;700&display=swap" rel="stylesheet">
<style>
:root{
  --orange:#ff6130;
  --ink:#111111;
  --muted:#555555;
  --night:#0d1420;
  --night-2:#1b2636;
  --card:#f5f5f5;
  --line:#e6e6e6;
  --white:#ffffff;
}
*{box-sizing:border-box;margin:0;padding:0}
html,body{width:1200px;height:3154px;overflow:hidden}
body{font-family:"Poppins",sans-serif;color:var(--ink);background:var(--white);position:relative}
.btn{display:inline-flex;align-items:center;justify-content:center;background:var(--orange);color:var(--white);font-weight:600;font-size:15px;border-radius:24px;text-decoration:none}
h2,h3{font-family:"Figtree",sans-serif}

/* hero */
.hero{position:absolute;left:0;top:0;width:1200px;height:675px;background:radial-gradient(circle at 70% 45%,#4a3b32 0%,#1f1d22 38%,var(--night) 75%)}
.hero-media{position:absolute;right:0;top:0;width:620px;height:675px;background:radial-gradient(ellipse at 55% 55%,#8a6a55 0%,#3b2f2b 45%,transparent 75%)}
.nav{position:absolute;left:60px;top:10px;width:1080px;height:71px;background:var(--white);border-radius:36px;display:flex;align-items:center;padding:0 22px 0 36px}
.nav-links{display:flex;gap:40px;font-size:13px}
.nav-links a{color:var(--ink);text-decoration:none}
.brand{position:absolute;left:50%;transform:translateX(-50%);display:flex;flex-direction:column;align-items:center;line-height:1}
.brand b{font-family:"Figtree",sans-serif;font-weight:700;font-size:22px;color:var(--ink)}
.brand small{font-size:6px;letter-spacing:2px;font-weight:600;margin-top:2px}
.nav-right{margin-left:auto;display:flex;align-items:center;gap:20px}
.login{display:flex;align-items:center;gap:8px;font-weight:600;font-size:15px}
.nav .btn{width:150px;height:42px}
.hero-copy{position:absolute;left:61px;top:225px;color:var(--white)}
.hero-copy h1{font-weight:300;font-size:46px;line-height:55px;letter-spacing:.5px}
.hero-copy h1 strong{font-weight:600;font-size:48px;display:block;margin-top:2px}
.hero-copy p{font-size:15px;margin-top:22px}
.hero-copy .btn{width:150px;height:41px;margin-top:30px}

/* become */
.become{position:absolute;left:0;top:675px;width:1200px;height:752px}
.become h2{text-align:center;font-size:31px;font-weight:600;margin-top:72px}
.become .lead{text-align:center;font-size:13px;color:var(--muted);line-height:19px;width:660px;margin:16px auto 0}
.card{position:absolute;width:525px;height:232px;background:var(--card);border-radius:14px;overflow:hidden;display:flex}
.card-media{width:262px;height:100%;flex:none}
.card-body{padding:0 10px 0 34px;display:flex;flex-direction:column;justify-content:center}
.card-body h3{font-size:18px;font-weight:600;line-height:23px}
.card-body p{font-size:12.5px;color:var(--muted);line-height:19.5px;margin-top:10px;max-width:200px}
.c1{left:60px;top:198px}.c2{left:615px;top:198px}.c3{left:60px;top:445px}.c4{left:615px;top:445px}
.m1{background:linear-gradient(135deg,#b89d78,#4e5447)}
.m2{background:linear-gradient(135deg,#0c2227,#2f6b5f 60%,#b8633e)}
.m3{background:linear-gradient(135deg,#e8e8e6,#9a9d9f)}
.m4{background:linear-gradient(135deg,#4a4c4e,#b4a898)}

/* founders */
.founders{position:absolute;left:0;top:1427px;width:1200px;height:437px;display:flex}
.founders-copy{width:600px;background:var(--orange);color:var(--white);padding:74px 0 0 61px}
.founders-copy h2{font-size:30px;font-weight:600}
.founders-copy p{font-size:12.5px;line-height:21px;width:420px;margin-top:14px}
.founders-copy p+p{margin-top:6px}
.btn-outline{display:inline-flex;align-items:center;justify-content:center;width:151px;height:42px;border:1.5px solid var(--white);border-radius:24px;color:var(--white);font-weight:600;font-size:15px;margin-top:30px}
.founders-media{width:600px;background:radial-gradient(ellipse at 45% 45%,#4b6c8c 0%,#1d2a3a 50%,#0b0f16 90%)}

/* economics */
.economics{position:absolute;left:0;top:1864px;width:1200px;height:377px}
.economics h2{text-align:center;font-size:31px;font-weight:600;margin-top:74px}
.stats{position:absolute;left:164px;top:145px;display:flex;gap:21px}
.stat{width:157px;height:157px;border:1px solid var(--line);display:flex;flex-direction:column;align-items:center;justify-content:center;text-align:center}
.stat b{font-size:37px;font-style:italic;font-weight:700;line-height:40px}
.stat span{font-size:15px;font-weight:600;color:#4a4a4a;line-height:24px;margin-top:4px}

/* cta */
.cta{position:absolute;left:0;top:2241px;width:1200px;height:389px;background:linear-gradient(90deg,#0a0f17 0%,#1a2638 45%,#22344c 100%)}
.cta-media{position:absolute;left:80px;top:0;width:460px;height:389px;background:radial-gradient(ellipse at 50% 55%,#3a3530 0%,#171b22 60%,transparent 85%)}
.cta-copy{position:absolute;left:671px;top:132px;color:var(--white)}
.cta-copy h2{font-size:31px;font-weight:600}
.cta-copy p{font-size:13px;margin-top:14px}
.cta-copy .btn{width:150px;height:41px;margin-top:26px;margin-left:4px}

/* partners */
.partners{position:absolute;left:0;top:2630px;width:1200px;height:213px;display:flex;align-items:center}
.partners h2{font-size:30px;font-weight:600;line-height:36px;margin-left:62px;width:300px}
.partner-row{display:flex;margin-left:0}
.partner{width:198px;height:96px;display:flex;align-items:center;justify-content:center;font-family:"Figtree",sans-serif;font-weight:700;font-size:23px;color:#9b9b9b;border-left:1px solid var(--line)}
.partner:first-child{border-left:none}

/* footer */
.footer{position:absolute;left:0;top:2843px;width:1200px;height:311px;background:var(--ink);color:var(--white)}
.f-brand{position:absolute;left:62px;top:54px;line-height:1}
.f-brand b{font-family:"Figtree",sans-serif;font-weight:700;font-size:21px}
.f-brand small{display:block;font-size:6px;letter-spacing:2px;margin-top:2px}
.socials{position:absolute;left:60px;top:112px;display:flex;gap:8px}
.socials span{width:36px;height:36px;border:1.5px solid var(--orange);border-radius:50%}
.f-col{position:absolute;top:54px}
.f-col h4{color:var(--orange);font-family:"Poppins",sans-serif;font-size:18px;font-weight:600}
.links{left:335px}
.links a{display:block;color:var(--white);text-decoration:none;font-size:13px;margin-top:14px}
.links a:first-of-type{margin-top:18px}
.contact{left:609px}
.contact li{list-style:none;display:flex;align-items:center;gap:16px;font-size:13px;margin-top:16px;line-height:24px}
.contact li:first-of-type{margin-top:14px}
.ic{width:36px;height:36px;border:1.5px solid var(--orange);border-radius:50%;display:flex;align-items:center;justify-content:center;flex:none}
.news{left:882px}
.news label{display:block;font-size:12px;margin-top:18px}
.news .field{width:262px;height:43px;border:1px solid #cfcfcf;border-radius:22px;margin-top:12px;margin-left:-2px}
.news .btn{width:135px;height:41px;margin-top:14px}
.f-rule{position:absolute;left:60px;top:262px;width:1080px;height:1px;background:#333}
.copy{position:absolute;left:0;top:280px;width:1200px;text-align:center;font-size:12px}
</style>
</head>
<body>

<header class="hero">
  <div class="hero-media" role="img" aria-label="Hero video: a smiling woman in a white vest reading a tablet against a night city skyline"></div>
  <nav class="nav">
    <div class="nav-links"><a href="#">Home</a><a href="#">Join Vc</a><a href="#">Startups</a></div>
    <div class="brand"><b>Lateshift</b><small>VENTURES</small></div>
    <div class="nav-right">
      <span class="login">
        <svg width="22" height="22" viewBox="0 0 22 22" fill="none" stroke="#111" stroke-width="1.6"><circle cx="11" cy="11" r="9.5"/><circle cx="11" cy="9" r="3.2"/><path d="M5 17.5c1.5-2.5 3.5-3.5 6-3.5s4.5 1 6 3.5"/></svg>
        Log In
      </span>
      <a class="btn" href="#">Get Started</a>
    </div>
  </nav>
  <div class="hero-copy">
    <h1>Venture Capital for<br>the late night<strong>hustlers</strong></h1>
    <p>Become a Venture Capital Investor</p>
    <a class="btn" href="#">Get Started</a>
  </div>
</header>

<section class="become">
  <h2>Become a VC</h2>
  <p class="lead">At Lateshift Ventures, we're opening the doors to a new kind of investor, mid-career professionals and aspiring VCs who want real skin in the game, not just exposure from the sidelines.</p>
  <article class="card c1">
    <div class="card-media m1" role="img" aria-label="Team meeting around a table in a bright office"></div>
    <div class="card-body"><h3>Hands on VC Work</h3><p>Each Lateshift Investor can actively be involved in sourcing, evaluating, and making key investment decisions as little or as much as they want.</p></div>
  </article>
  <article class="card c2">
    <div class="card-media m2" role="img" aria-label="Investor studying glowing market charts at night"></div>
    <div class="card-body"><h3>Meaningful Opportunities to develop your career in Venture Capital</h3><p>Lateshift Investors, depending on the level of commitment and involvement, can work at our fund as Partners.</p></div>
  </article>
  <article class="card c3">
    <div class="card-media m3" role="img" aria-label="Two colleagues reviewing figures on a laptop"></div>
    <div class="card-body"><h3>Earn Carry and Put Your Name on an Investment</h3><p>Earn carry interest based on the level of your involvement on each deal.</p></div>
  </article>
  <article class="card c4">
    <div class="card-media m4" role="img" aria-label="Group discussion in front of a whiteboard"></div>
    <div class="card-body"><h3>Join a community of Hustlers</h3><p>Network with likeminded investors, aspiring investors and limited partners.</p></div>
  </article>
</section>

<section class="founders">
  <div class="founders-copy">
    <h2>Simplifying success for founders</h2>
    <p>Our strength lies in our network. Our LPs and operating partners are all mid-to-senior level executives in their industries. They bring real-world corporate experience, offering strategic insights and operational support to help our portfolio companies scale efficiently.</p>
    <p>We cut through the noise and get to the core of your business fast. If we love what you're building, we'll move. If not, we'll tell you quickly and respectfully. That lets you make</p>
    <span class="btn-outline">Learn More</span>
  </div>
  <div class="founders-media" role="img" aria-label="Hand over a laptop with a rising growth chart projection"></div>
</section>

<section class="economics">
  <h2>Fund Economics</h2>
  <div class="stats">
    <div class="stat"><b>14</b><span>Pre-Seed / Seed<br>Investments</span></div>
    <div class="stat"><b>50K</b><span>Check<br>Size</span></div>
    <div class="stat"><b>20%</b><span>Carried<br>Interest</span></div>
    <div class="stat"><b>2.5%</b><span>Management<br>Fee</span></div>
    <div class="stat"><b>1M</b><span>Fund<br>Size</span></div>
  </div>
</section>

<section class="cta">
  <div class="cta-media" role="img" aria-label="Man working on a laptop in front of a night city view"></div>
  <div class="cta-copy">
    <h2>Ready to start investing as a VC?</h2>
    <p>Book an interview to learn more and see if you qualify.</p>
    <a class="btn" href="#">Get Started</a>
  </div>
</section>

<section class="partners">
  <h2>Fund<br>Economics</h2>
  <div class="partner-row">
    <div class="partner">Varnwick</div>
    <div class="partner">Tessel</div>
    <div class="partner">Orvane</div>
    <div class="partner">Quillby</div>
  </div>
</section>

<footer class="footer">
  <div class="f-brand"><b>Lateshift</b><small>VENTURES</small></div>
  <div class="socials" aria-label="Social links"><span></span><span></span><span></span></div>
  <div class="f-col links">
    <h4>Links</h4>
    <a href="#">Solutions</a><a href="#">Vision</a><a href="#">Programs</a><a href="#">Blog</a>
  </div>
  <ul class="f-col contact">
    <h4>Contact Us</h4>
    <li><span class="ic"><svg width="16" height="16" viewBox="0 0 24 24" fill="none" stroke="#ff6130" stroke-width="1.8"><path d="M5 3h4l2 5-2.5 1.5a11 11 0 0 0 6 6L16 13l5 2v4a2 2 0 0 1-2 2A17 17 0 0 1 3 5a2 2 0 0 1 2-2z"/></svg></span>+ 555-014-2290</li>
    <li><span class="ic"><svg width="16" height="16" viewBox="0 0 24 24" fill="none" stroke="#ff6130" stroke-width="1.8"><rect x="3" y="5" width="18" height="14" rx="2"/><path d="M3 7l9 6 9-6"/></svg></span>hello@lateshift.example</li>
    <li><span class="ic"><svg width="16" height="16" viewBox="0 0 24 24" fill="none" stroke="#ff6130" stroke-width="1.8"><path d="M12 22s7-7 7-12a7 7 0 0 0-14 0c0 5 7 12 7 12z"/><circle cx="12" cy="10" r="2.5"/></svg></span>218 Harlow Lane Suite 4<br>Easton, CA 94012</li>
  </ul>
  <div class="f-col news">
    <h4>Our Newsletter</h4>
    <label>Email *</label>
    <div class="field"></div>
    <a class="btn" href="#">Submit</a>
  </div>
  <div class="f-rule"></div>
  <p class="copy">© 2025 lateshift ventures. all right reserved.</p>
</footer>

</body>
</html>
```